Pellston Ironstags Website

A revamp of the design @ pellstonfootball.com.

Colors and logos must remain same, as does the content and schedules. But we would like a new look to the whole thing.

```html
<!DOCTYPE html>
<html lang="en">
<head>
<meta charset="utf-8">
<title>Pellston Ironstags</title>
<link rel="stylesheet" href="https://fonts.googleapis.com/css2?family=Arimo:wght@400;700&display=swap">
<style>
:root{
  --red:#e00d0d;
  --red-dark:#a80000;
  --header:#0d1117;
  --panel:rgba(20,24,20,.82);
  --panel-line:rgba(255,255,255,.28);
  --frame:#cfd6cf;
  --text:#ffffff;
  --muted:#c9cfc9;
  --field-dark:#0b0d0c;
  --grass:#3f8c1e;
}
*{box-sizing:border-box;margin:0;padding:0}
html,body{width:1200px;height:918px;overflow:hidden}
body{position:relative;font-family:"Arimo",Arial,sans-serif;color:var(--text);
  background:linear-gradient(180deg,#1b2630 0%,#3e5668 20%,#2d4a2c 36%,#4f9d25 55%,#3a7f1a 80%,#244f12 100%)}
.abs{position:absolute}
.site-header{left:0;top:0;width:1200px;height:130px;background:linear-gradient(180deg,#151b22,#0a0d11)}
.header-stripe{left:0;top:118px;width:1200px;height:9px;background:var(--red);border-top:2px solid #6e7da0}
.brand-box{left:151px;top:0;width:121px;height:128px;background:#fff;display:flex;align-items:center;justify-content:center;color:#111;font-weight:700;font-size:17px}
.site-title{left:293px;top:18px;font-size:43px;font-weight:700;letter-spacing:.2px}
.site-subtitle{left:294px;top:62px;font-size:22px;font-weight:700}
.admin-btn{left:898px;top:40px;width:144px;height:32px;background:var(--red);border-radius:4px;font-size:17px;display:flex;align-items:center;justify-content:center}
.breadcrumb{left:162px;top:149px;font-size:12px;color:#111}
.breadcrumb u{margin-left:6px}
.utility{right:168px;top:149px;font-size:12px;color:#111}
.main-frame{left:156px;top:178px;width:883px;height:674px;border:3px solid var(--frame);border-radius:12px;background:rgba(10,14,10,.35)}
.ad{display:flex;align-items:center;justify-content:center;font-size:11px;color:rgba(255,255,255,.55)}
.ad-banner{left:176px;top:198px;width:683px;height:84px;background:linear-gradient(90deg,#b02a1a 0%,#1d3f8a 14%,#1d3f8a 24%,#6a1010 30%,#3a0909 70%,#2a1a12 100%)}
.ad-tower{left:871px;top:198px;width:150px;height:562px;background:linear-gradient(180deg,#000 0%,#0a0a12 60%,#1a1020 100%);border:1px solid #333}
.ad-badge{left:871px;top:772px;width:150px;height:57px;background:#c9b993;border:1px solid #444}
.menu-panel{left:157px;top:344px;width:195px;height:473px;background:var(--panel);border-right:1px solid var(--panel-line)}
.box-head{background:var(--red);border-radius:4px 4px 0 0;font-size:19px;display:flex;align-items:center;padding-left:20px}
.menu-head{left:149px;top:302px;width:201px;height:42px}
.menu-list{left:179px;top:355px;list-style:none;font-size:12px}
.menu-list li{height:25.4px;line-height:25.4px}
.menu-list li::before{content:"›";margin-right:11px;color:#ddd}
.welcome-head{left:364px;top:302px;width:496px;height:44px}
.welcome-body{left:364px;top:346px;width:496px;height:196px;background:var(--panel);border:1px solid var(--panel-line);border-top:0;padding:20px 0 0 22px;font-size:17.5px;line-height:21px}
.welcome-body p{margin-bottom:16px}
.search-box{left:364px;top:556px;width:496px;height:98px;background:var(--panel);border:1px solid var(--panel-line);border-radius:4px;padding:10px 12px;font-size:13px;line-height:17px}
.field{background:var(--field-dark);border-radius:3px;font-size:11px;color:#8a8f8a;display:flex;align-items:center}
.search-field{left:376px;top:611px;width:378px;height:29px;padding-left:12px}
.search-field svg{margin-right:14px}
.btn-red{background:var(--red);border-radius:3px;display:flex;align-items:center;justify-content:center}
.search-btn{left:766px;top:611px;width:82px;height:29px;font-size:13px}
.news-box{left:364px;top:667px;width:352px;height:107px;background:var(--panel);border:1px solid var(--panel-line);border-radius:4px;padding:8px 14px}
.news-title{font-size:15px;margin-bottom:6px}
.news-text{font-size:9.5px;line-height:12px;color:#e8e8e8}
.news-field{left:377px;top:733px;width:229px;height:28px;padding-left:10px}
.news-field svg{margin-right:14px}
.news-btn{left:616px;top:733px;width:70px;height:28px;font-size:11px}
.season-box{left:733px;top:684px;width:109px;height:76px;background:var(--red);border:2px solid #f2b0b0;border-radius:3px;text-align:center;font-weight:700}
.season-box .year{font-size:34px;line-height:36px;margin-top:6px}
.season-box .label{font-size:14px}
.like-row{left:366px;top:794px;display:flex;align-items:center;font-size:9.5px}
.like-btn{display:flex;align-items:center;gap:4px;background:#eef0f5;color:#3b5080;border:1px solid #b9c0d0;border-radius:3px;padding:3px 6px;margin-right:8px}
.sq{width:10px;height:10px;background:#3b5998;display:inline-block;margin-right:6px}
.follow{left:695px;top:801px;display:flex;align-items:center;font-size:15px}
.follow span.icon{width:14px;height:14px;margin-left:10px;display:inline-block;border-radius:2px}
.copyright{left:0;width:1200px;top:872px;text-align:center;font-size:10px;color:#111}
</style>
</head>
<body>
<header class="abs site-header"></header>
<div class="abs header-stripe"></div>
<div class="abs brand-box">Ironstags</div>
<h1 class="abs site-title">Pellston Ironstags</h1>
<p class="abs site-subtitle">Pellston Independent Football Association</p>
<div class="abs admin-btn">Administration</div>

<div class="abs breadcrumb">Pellston Independent Football Association &gt; <u>www.pellstonfootball.com</u></div>
<div class="abs utility">Video Training | Weather</div>

<main class="abs main-frame"></main>

<div class="abs ad ad-banner" role="img" aria-label="Civic Reserve career training advertisement banner with athlete photo and Learn More button"></div>
<div class="abs ad ad-tower" role="img" aria-label="Drillhouse basic training advertisement with workout photo, military-style workouts, presented by Civic Reserve"></div>
<div class="abs ad ad-badge" role="img" aria-label="Partner magazine badge"></div>

<nav class="abs menu-panel"></nav>
<div class="abs box-head menu-head">PIFA Main Menu</div>
<ul class="abs menu-list">
  <li>Welcome</li><li>Football</li><li>7 on 7 Football</li><li>Cheer</li><li>Calendar</li>
  <li>Division/Leagues</li><li>Teams/Rosters</li><li>Schedules</li><li>Standings</li><li>Game Results</li>
  <li>Contact Info</li><li>Links</li><li>Sponsors</li><li>Tournaments</li><li>Directions</li>
  <li>Photo Albums</li><li>Forms/Handouts</li><li>Our Classifieds</li>
</ul>

<div class="abs box-head welcome-head">Welcome to Pellston Ironstags</div>
<section class="abs welcome-body">
  <p>Pellston Ironstags 2011 Football Season has started.</p>
  <p>Come out and see what everybody is talking about!!<br>"Your Pellston Ironstags"</p>
  <p>Come enjoy some Football &amp; Cheerleading while supporting<br>your Pellston Ironstags!<br>Home games are played at Marlow Ridge Middle School.</p>
</section>

<section class="abs search-box">This search page allows you to search news articles on the Pellston Independent Football Association site for any exact word or phrase.</section>
<div class="abs field search-field">
  <svg width="12" height="12" viewBox="0 0 12 12"><circle cx="7" cy="5" r="3.5" fill="none" stroke="#888" stroke-width="1.4"/><line x1="4.5" y1="7.5" x2="1" y2="11" stroke="#888" stroke-width="1.6"/></svg>
  Enter a search word or phrase:
</div>
<div class="abs btn-red search-btn">Search</div>

<section class="abs news-box">
  <div class="news-title">Newsletter Signup</div>
  <p class="news-text">Sign up to our newsletter and receive regular updates on the latest Ironstags related products and articles directly to your inbox!</p>
</section>
<div class="abs field news-field">
  <svg width="14" height="10" viewBox="0 0 14 10"><rect width="14" height="10" rx="1" fill="#e0b020"/><path d="M0 0 L7 6 L14 0" fill="none" stroke="#8a6a00" stroke-width="1.2"/></svg>
  enter your E-mail Address here
</div>
<div class="abs btn-red news-btn">Subscribe</div>

<div class="abs season-box"><div class="year">2011</div><div class="label">Season Info</div></div>

<div class="abs like-row">
  <span class="like-btn"><span class="sq" style="margin-right:0"></span>Like</span>
  <span class="sq"></span>Be the first of your friends to like this.
</div>
<div class="abs follow">Follow Us On:
  <span class="icon" style="background:#3b5998"></span>
  <span class="icon" style="background:#33aadd"></span>
  <span class="icon" style="background:#c4302b"></span>
</div>

<footer class="abs copyright">© Copyright Brightwire Studio 2011. All Rights Reserved.</footer>
</body>
</html>
```